HomePage Design for Lumen Getaways - once-in-a-lifetime experiences for busy working people

Design a homepage for the Lumen Getaways (www.lumengetaways.example) website compatible with further web pages and the design briefing documents attached

LG HomePage Design Brief
We are seeking website HomePage designs incorporating our new Logo and colour scheme, for Lumen Getaways (www.lumengetaways.example) to go with the site functionality and wireframe ideas attached.
The website HomePage design needs to
• Incorporate and be consistent with the LG Logo and its colour scheme attached.
• Express the brand values of being inspirational, high quality, upscale, cultured, aspirational, and contemporary – even somewhat ‘hip’. Probably positioned somewhere between Harlow Pike (Deluxe Travel) and Green Walrus (Hip Travel) – see https://www.harlowpike.example and https://www.greenwalrus.example .
• Be instantly recognisable and different from other travel websites and instantly communicate the nature of the brand proposition and target customer base.
• Appeal to our core 25-55 affluent businesspeople demographic
• Work in the UK, US/Canada and Australia/NZ and ultimately in mainland Europe.
• Use fonts and colours that are easily reproduced online and compatible with nearly all browsers.
• Be part of a responsive website design, that can be used both on Desktops and laptops but also with tablets and mobile ‘phones (hence content not too wide across the page)
• Feature the strapline ‘Lumen Getaways in less than 7 Days’
• Work with the and wireframes and processes shown in the attached presentation – although intended as a guide only these features and processes all need to be incorporated into the HomePage.
• Make full use of high quality images and video to convey our brand proposition and products

Target Market(s)

25-55 affluent businesspeople

Industry/Entity Type

Travel Industry

Number of Pages Required

1 page

Font styles to use
Sans Serif

Colors
0455a3
00a88f

Requirements
Must have
• • Incorporate and be consistent with the LG Logo and its colour scheme attached.
• • Express the brand values of being inspirational, high quality, upscale, cultured, aspirational, and contemporary – even somewhat ‘hip’. Probably positioned somewhere between Harlow Pike (Deluxe Travel) and Green Walrus (Hip Travel) – see https://www.harlowpike.example and https://www.greenwalrus.example .
• • Be instantly recognisable and different from other travel websites and instantly communicate the nature of the brand proposition and target customer base.
• • Appeal to our core 25-55 affluent businesspeople demographic
• • Be part of a responsive website design, that can be used both on Desktops and laptops but also with tablets and mobile ‘phones (hence content not too wide across the page)
• • Feature the strapline ‘Lumen Getaways in less than 7 Days’
• • Work with the and wireframes and processes shown in the attached presentation – although intended as a guide only these features and processes all need to be incorporated into the HomePage.
• • Make full use of high quality images and video to convey our brand proposition and products
• Colours as per Logo not as shown below
Nice to have
• • Work in the UK, US/Canada and Australia/NZ and ultimately in mainland Europe.
Should not have
• Must not be cheap or mass-market, nor excessively "stuffy or luxury-orientated"

```html
<!DOCTYPE html>
<html lang="en">
<head>
<meta charset="utf-8">
<title>Lumen Getaways – Home</title>
<link href="https://fonts.googleapis.com/css2?family=Lato:wght@400;700&display=swap" rel="stylesheet">
<style>
:root{
  --navy:#2b3177;
  --green:#1d5f2b;
  --green-title:#2a6a1e;
  --panel:#e4e4e4;
  --text:#444;
  --dark:#3a3a3a;
  --white:#fff;
}
*{margin:0;padding:0;box-sizing:border-box}
html,body{width:908px;height:1200px;overflow:hidden;background:#fff;font-family:'Lato',sans-serif;color:var(--text)}
.page{position:relative;width:908px;height:1200px}
.abs{position:absolute}

.brand{left:0;width:908px;top:52px;text-align:center;color:var(--green);font-size:20px;font-weight:700;letter-spacing:1px;display:flex;justify-content:center;align-items:center;gap:8px}
.brand .dot{width:12px;height:12px;border-radius:50%;background:var(--navy)}
.social-ribbons{left:678px;top:0;display:flex;gap:12px}
.social-ribbons svg{display:block}

.hero{left:0;top:120px;width:908px;height:334px;background:linear-gradient(180deg,#3cc6f0 0%,#8fdcf5 55%,#d8eef4 75%,#6b8f4a 92%,#3c7a2c 100%)}

.main-nav{left:0;top:454px;width:908px;height:44px;background:var(--navy);box-shadow:0 3px 4px rgba(0,0,0,.25)}
.main-nav a{position:absolute;top:0;line-height:44px;color:var(--white);text-decoration:none;font-size:11.5px}
.main-nav .sep{position:absolute;top:0;width:1px;height:44px;background:rgba(255,255,255,.15)}
.login{position:absolute;left:747px;top:9px;width:101px;height:28px;background:var(--white);border-radius:4px;color:var(--navy);font-size:11.5px;text-align:center;line-height:28px}

.intro-title{left:64px;top:527px;color:var(--green);font-size:19px;letter-spacing:1.6px;font-weight:400}
.exp-panel{left:62px;top:562px;width:538px;height:340px;background:var(--panel)}
.card{position:absolute;width:126px;text-align:center}
.card .photo{width:126px;height:64px}
.card h3{color:var(--green-title);font-size:9px;font-weight:700;margin-top:7px;line-height:1.15}
.card p{font-size:7.6px;line-height:1.35;margin:6px 8px 0;color:#555}
.card .more{display:inline-block;margin-top:6px;border:1px solid var(--navy);color:var(--navy);font-size:7px;padding:1px 5px;background:#fff}
.card .more.active{background:var(--navy);color:#fff}

.places-head{left:616px;top:521px;width:240px;height:34px;background:var(--navy);color:#fff;font-size:18px;text-align:center;line-height:34px;font-weight:700}
.places-panel{left:616px;top:562px;width:240px;height:340px;background:var(--panel)}
.place{position:absolute;left:10px;width:222px;height:105px}
.place span{position:absolute;left:0;bottom:0;width:100%;height:18px;line-height:18px;background:rgba(20,20,20,.75);color:#fff;font-size:9px;font-weight:700;text-align:center}

.partners{left:0;top:948px;width:908px;height:40px}
.partner{position:absolute;top:8px;font-size:15px;color:#111}
.partner.bold{font-weight:700;font-size:14px;top:8px}

.site-footer{left:0;top:1034px;width:908px;height:130px;background:var(--navy)}
.foot-col{position:absolute;top:28px;list-style:none}
.foot-col li{color:#fff;font-size:10.5px;line-height:18.3px}
.legal{left:0;top:1164px;width:908px;height:36px;background:var(--dark)}
.legal p{position:absolute;left:63px;top:11px;color:#fff;font-size:10.5px;letter-spacing:.4px}
.legal .icons{position:absolute;left:728px;top:8px;display:flex;gap:7px}
.legal .icons i{width:19px;height:19px;border-radius:50%;background:#fff;display:block}
</style>
</head>
<body>
<div class="page">

  <header>
    <div class="abs brand"><span class="dot"></span>Lumen Getaways</div>
    <div class="abs social-ribbons" aria-label="Social links">
      <svg width="24" height="38" viewBox="0 0 24 38"><path d="M0 0H24V38L12 33L0 38Z" fill="#3aaee0"/></svg>
      <svg width="24" height="38" viewBox="0 0 24 38"><path d="M0 0H24V38L12 33L0 38Z" fill="#e0457b"/></svg>
      <svg width="24" height="38" viewBox="0 0 24 38"><path d="M0 0H24V38L12 33L0 38Z" fill="#2b4a8b"/></svg>
      <svg width="24" height="38" viewBox="0 0 24 38"><path d="M0 0H24V38L12 33L0 38Z" fill="#1fb3df"/></svg>
      <svg width="24" height="38" viewBox="0 0 24 38"><path d="M0 0H24V38L12 33L0 38Z" fill="#e8432e"/></svg>
    </div>
  </header>

  <div class="abs hero" role="img" aria-label="World landmarks skyline with an aeroplane flying across a bright blue sky"></div>

  <nav class="abs main-nav">
    <a style="left:63px">Destinations</a><span class="sep" style="left:145px"></span>
    <a style="left:159px">Experiences</a><span class="sep" style="left:235px"></span>
    <a style="left:252px">Trips by Month</a><span class="sep" style="left:345px"></span>
    <a style="left:362px">Topical Now</a><span class="sep" style="left:443px"></span>
    <a style="left:458px">Tailored</a><span class="sep" style="left:512px"></span>
    <a style="left:528px">Pioneers Club</a><span class="sep" style="left:615px"></span>
    <a style="left:633px">Vlogs &amp; Reviews</a>
    <span class="login">CLIENT LOG-IN</span>
  </nav>

  <h1 class="abs intro-title">Lumen Getaways in less than 7 Days!</h1>

  <section class="abs exp-panel">
    <div class="card" style="left:7px;top:9px">
      <div class="photo" role="img" aria-label="Elephants on the savannah" style="background:linear-gradient(#8a8f94,#7a6a4e)"></div>
      <h3>Wonders of Wildlife</h3>
      <p>Lorem Ipsum is simply dummy text printing and typesetting industry</p>
      <span class="more">Read More</span>
    </div>
    <div class="card" style="left:139px;top:9px">
      <div class="photo" role="img" aria-label="Festival crowd under red stage lights" style="background:linear-gradient(#e8354a,#b0201e)"></div>
      <h3>Experiences</h3>
      <p>Lorem Ipsum is simply dummy text printing and typesetting industry</p>
      <span class="more">Read More</span>
    </div>
    <div class="card" style="left:271px;top:9px">
      <div class="photo" role="img" aria-label="Brown bear in the wild" style="background:linear-gradient(#8c8a80,#5a4634)"></div>
      <h3>Must Do Activities</h3>
      <p>Lorem Ipsum is simply dummy text printing and typesetting industry</p>
      <span class="more">Read More</span>
    </div>
    <div class="card" style="left:401px;top:9px">
      <div class="photo" role="img" aria-label="Hot air balloon at sunset" style="background:linear-gradient(#6a4a6e,#d8744a 70%,#2a1a20)"></div>
      <h3>Unique Annual Events</h3>
      <p>Lorem Ipsum is simply dummy text printing and typesetting industry</p>
      <span class="more active">Read More</span>
    </div>
    <div class="card" style="left:84px;top:180px">
      <div class="photo" role="img" aria-label="Green mountain valley" style="background:linear-gradient(#6f9ac4,#4f8a2e 55%,#2f5e1a)"></div>
      <h3>Extraordinary &amp; Secret Places</h3>
      <p>Lorem Ipsum is simply dummy text printing and typesetting industry</p>
      <span class="more">Read More</span>
    </div>
    <div class="card" style="left:216px;top:180px">
      <div class="photo" role="img" aria-label="Dancers performing on a dark stage" style="background:linear-gradient(#0b1020,#1a2030)"></div>
      <h3>Unforgettable Performances</h3>
      <p>Lorem Ipsum is simply dummy text printing and typesetting industry</p>
      <span class="more">Read More</span>
    </div>
    <div class="card" style="left:348px;top:180px">
      <div class="photo" role="img" aria-label="Climber on a rocky ridge" style="background:linear-gradient(#b8c4cc,#6e7274)"></div>
      <h3>Spectacular Hiking,<br>Climbing &amp; Walking</h3>
      <p>Lorem Ipsum is simply dummy text printing and typesetting industry</p>
      <span class="more">Read More</span>
    </div>
  </section>

  <aside>
    <h2 class="abs places-head">Last Few Places</h2>
    <div class="abs places-panel">
      <div class="place" style="top:9px;background:linear-gradient(90deg,#8aa6bf,#6a3a8a)" role="img" aria-label="Venice carnival masks by the lagoon"><span>Venice Carnival £599pp</span></div>
      <div class="place" style="top:116px;background:linear-gradient(#7d8f96,#5c7040)" role="img" aria-label="Stone statues on a grassy island hillside"><span>Easter Island £2,999pp</span></div>
      <div class="place" style="top:224px;background:linear-gradient(#3a2a20,#1a1210)" role="img" aria-label="Day of the Dead celebration at night"><span>Day of the Dead £3,299pp</span></div>
    </div>
  </aside>

  <section class="abs partners" aria-label="Partners">
    <span class="partner" style="left:63px">Harlow Pike</span>
    <span class="partner bold" style="left:207px">GREEN WALRUS</span>
    <span class="partner" style="left:350px">Harlow Pike</span>
    <span class="partner bold" style="left:495px">GREEN WALRUS</span>
    <span class="partner" style="left:646px">Harlow Pike</span>
    <span class="partner bold" style="left:791px">GREEN WALRUS</span>
  </section>

  <footer>
    <div class="abs site-footer">
      <ul class="foot-col" style="left:63px"><li>About Us</li><li>Our Partners</li><li>Newsletter</li><li>FAQs</li></ul>
      <ul class="foot-col" style="left:186px"><li>Contact Us</li><li>Booking Conditions</li><li>Privacy &amp; Cookies</li><li>Terms of Use</li></ul>
      <ul class="foot-col" style="left:338px"><li>Financial Protection</li><li>Travel</li><li>Visas</li><li>Travel Advice</li></ul>
      <ul class="foot-col" style="left:496px"><li>Group booking</li><li>Tailor-Made &amp; Extra Nights</li><li>Booking Fights</li><li>Careers with LG</li></ul>
      <ul class="foot-col" style="left:679px"><li>LG Protecting eildlife &amp; animals,</li><li>and Supporting local communities</li><li>Prsss Room</li></ul>
    </div>
    <div class="abs legal">
      <p>Privacy policy - Legal mentions - Terms and Conditions</p>
      <div class="icons" aria-label="Social links"><i></i><i></i><i></i><i></i><i></i></div>
    </div>
  </footer>

</div>
</body>
</html>
```